Pedalwise Touring Co Brochure

We need an informational brochure designed to display all of our cycling tours for the 2019 season. The majority of text and images can be pulled from our website - www.pedalwisetouringco.example

We would like to use the colors red (#242424), Grey, and White

```html
<!DOCTYPE html>
<html lang="en">
<head>
<meta charset="utf-8">
<title>Pedalwise Touring Co Brochure</title>
<link rel="stylesheet" href="https://fonts.googleapis.com/css2?family=Bebas+Neue&family=Roboto:wght@400;500;700&display=swap">
<style>
  :root {
    --brand-red: #c0253a;
    --brand-red-deep: #a81d31;
    --ink: #242424;
    --grey-light: #e4e4e6;
    --grey-mid: #c9c9cc;
    --white: #ffffff;
    --page-bg: #ffffff;
  }
  * { box-sizing: border-box; margin: 0; padding: 0; }
  html, body { width: 842px; height: 1200px; overflow: hidden; background: var(--page-bg); }
  body { position: relative; font-family: "Roboto", Arial, sans-serif; color: var(--ink); }

  .spread { position: absolute; box-shadow: 0 3px 10px rgba(0,0,0,0.22); background: var(--white); overflow: hidden; }
  .spread--cover { left: 127px; top: 127px; width: 586px; height: 415px; }
  .spread--inside { left: 127px; top: 598px; width: 594px; height: 418px; }

  .headline { font-family: "Bebas Neue", "Arial Narrow", sans-serif; font-weight: 400; line-height: 0.9; }

  /* Back cover */
  .back-cover { position: absolute; left: 0; top: 0; width: 293px; height: 415px; background: var(--brand-red); }
  .back-cover__photo { position: absolute; left: 0; top: 0; width: 293px; height: 250px;
    background: linear-gradient(170deg, #c7545f 0%, #b8313f 40%, #c0253a 100%); opacity: 0.9; }
  .brand { position: absolute; display: flex; align-items: center; gap: 7px; font-weight: 700; }
  .brand__mark { width: 32px; height: 32px; border-radius: 50%; border: 2px solid currentColor; flex: none; }
  .brand__name { font-size: 15px; line-height: 1.05; width: 110px; }
  .back-cover .brand { left: 78px; top: 278px; color: var(--white); }
  .back-cover__contact { position: absolute; left: 0; top: 356px; width: 293px; text-align: center;
    color: var(--white); font-size: 9px; font-weight: 500; line-height: 15px; }

  /* Front cover */
  .front-cover { position: absolute; left: 293px; top: 0; width: 293px; height: 415px; background: var(--white); }
  .front-cover__photo { position: absolute; left: 0; top: 0; width: 293px; height: 328px;
    background: linear-gradient(160deg, #e9e2c4 0%, #a9a35a 35%, #5f7a2a 65%, #2f3d18 100%); }
  .front-cover__title { position: absolute; left: 14px; top: 36px; color: var(--white); }
  .front-cover__title .line-one { font-size: 50px; display: block; }
  .front-cover__title .line-two { font-size: 26px; display: block; margin-top: 2px; }
  .front-cover__tagline { position: absolute; left: 14px; top: 104px; width: 160px;
    color: var(--white); font-size: 9px; line-height: 1.2; }
  .front-cover .brand { left: 86px; top: 342px; color: var(--brand-red); }
  .front-cover .brand__mark { width: 28px; height: 28px; }
  .front-cover .brand__name { font-size: 13px; }
  .front-cover__url { position: absolute; left: 0; top: 389px; width: 293px; text-align: center;
    font-size: 8px; font-weight: 500; }

  /* Inside left: story */
  .story { position: absolute; left: 0; top: 0; width: 297px; height: 418px; }
  .story__photo { position: absolute; left: 0; top: 0; width: 297px; height: 239px;
    background: linear-gradient(175deg, #d8dcd6 0%, #a69a6e 30%, #7b7148 60%, #5d5937 100%); }
  .story__title { position: absolute; left: 16px; top: 205px; font-size: 36px; color: var(--ink); }
  .story__body { position: absolute; left: 16px; top: 255px; width: 270px; font-size: 7.6px; line-height: 1.35; }
  .story__body p + p { margin-top: 8px; }

  /* Inside right: departures */
  .departures { position: absolute; left: 297px; top: 0; width: 297px; height: 418px; }
  .departures__photo { position: absolute; left: 0; top: 0; width: 297px; height: 115px;
    background: linear-gradient(180deg, #6f8fb0 0%, #3f5f7e 40%, #8b7f6a 75%, #4a4238 100%); }
  .departures__title { position: absolute; left: 14px; top: 84px; font-size: 34px; color: var(--white); }
  .departures__summary-label { position: absolute; left: 14px; top: 118px; font-size: 9px; font-weight: 500; }
  .departures__summary { position: absolute; left: 14px; top: 131px; width: 272px; font-size: 7.6px; line-height: 1.33; }

  .date-grid { position: absolute; left: 20px; top: 248px; display: grid;
    grid-template-columns: repeat(3, 74px); column-gap: 17px; row-gap: 14px; }
  .date-card { height: 70px; background: linear-gradient(160deg, var(--grey-light), var(--grey-mid));
    border-radius: 2px; position: relative; box-shadow: 0 1px 2px rgba(0,0,0,0.15); }
  .date-card__price { height: 11px; background: var(--brand-red); color: var(--white);
    font-size: 6px; font-weight: 500; text-align: right; padding: 2px 5px 0 0; border-radius: 2px 2px 0 0; }
  .date-card__price small { font-size: 4px; margin-right: 2px; }
  .date-card__dates { position: absolute; left: 5px; top: 18px; font-size: 4.6px; font-weight: 700; line-height: 1.35; }
  .date-card__seats { position: absolute; left: 5px; top: 38px; font-size: 4.6px; font-weight: 700; }
  .date-card__book { position: absolute; right: 5px; bottom: 6px; background: var(--brand-red); color: var(--white);
    font-size: 4.4px; font-weight: 700; padding: 1.5px 4px; border-radius: 1px; }
</style>
</head>
<body>

<section class="spread spread--cover">
  <div class="back-cover">
    <div class="back-cover__photo" role="img" aria-label="Red-tinted coastal cliffs with a winding road and cyclists"></div>
    <div class="brand"><span class="brand__mark"></span><span class="brand__name">Pedalwise Touring Co</span></div>
    <div class="back-cover__contact">
      <p>410 Orchard Lane, Hollowbrook, CA 90000</p>
      <p>ride@pedalwisetouringco.example</p>
      <p>www.pedalwisetouringco.example</p>
    </div>
  </div>
  <div class="front-cover">
    <div class="front-cover__photo" role="img" aria-label="Cyclist standing with a bike on a sunlit grassy hillside"></div>
    <h1 class="front-cover__title headline"><span class="line-one">It's All</span><span class="line-two">About the Ride</span></h1>
    <p class="front-cover__tagline">Cycling and mountain bike adventures that turn your bucket list into a bike-it list</p>
    <div class="brand"><span class="brand__mark"></span><span class="brand__name">Pedalwise Touring Co</span></div>
    <p class="front-cover__url">www.pedalwisetouringco.example</p>
  </div>
</section>

<section class="spread spread--inside">
  <div class="story">
    <div class="story__photo" role="img" aria-label="Coastal hills with a winding road and a distant cyclist"></div>
    <h2 class="story__title headline">Our Story</h2>
    <div class="story__body">
      <p>Pedalwise Touring Co was born from decades of experience as North America's leading specialist tour operator and a lifelong passion for cycling and mountain biking. We wanted to create a series of tours made for bikers by bikers, that highlight not only the most famous rides in the country, but also our favorites.</p>
      <p>While we have some amazing colleagues in the industry, we've found many tours to be slowed down by lazy days and charcuterie. While there's always time for cold, hazy IPA's and bold Cabernets, we find they taste better after cruising some of the most incredible rides of your life. Our mantra, "It's all about the ride," emphasizes our desire to create unique itineraries that will test your abilities, and help you find your strongest flow.</p>
      <p>Pedalwise Touring Co is where passion meets experience.</p>
    </div>
  </div>

  <div class="departures">
    <div class="departures__photo" role="img" aria-label="Three cyclists with bikes on a rocky seashore"></div>
    <h2 class="departures__title headline">Departure Dates</h2>
    <h3 class="departures__summary-label">Trip Summary</h3>
    <p class="departures__summary">Southern Utah's canyon country is renowned for its incredible multi colored cliffs, valleys, red rock monoliths, and singletrack trails. Shaped by billions of years of erosion, this alien landscape emerged as a true adventurer's playground. Hundreds of miles of singletrack trails wind over smooth outcroppings of weathered sandstone, known as slickrock. The ideal riding surface for mountain biking, slickrock provides a high level of grip, and stability, allowing riders to conquer even the gnarliest of obstacles. Expect a smorgasbord of turns, quick drops, short climbs, and no shortage of technical features that will push your balance, and ability as a rider. Spectacular vistas lie around every corner, and the unique beauty and colors of Utah will leave you in awe.</p>

    <div class="date-grid">
      <article class="date-card"><div class="date-card__price"><small>FROM</small>US $2395</div>
        <p class="date-card__dates">JUNE 9TH, 2019<br>JUNE 14TH, 2019</p><p class="date-card__seats">4+ SEATS LEFT</p><span class="date-card__book">BOOK NOW</span></article>
      <article class="date-card"><div class="date-card__price"><small>FROM</small>US $2395</div>
        <p class="date-card__dates">JUNE 16TH, 2019<br>JUNE 21TH, 2019</p><p class="date-card__seats">4+ SEATS LEFT</p><span class="date-card__book">BOOK NOW</span></article>
      <article class="date-card"><div class="date-card__price"><small>FROM</small>US $2395</div>
        <p class="date-card__dates">JULY 21ST, 2019<br>JULY 26TH, 2019</p><p class="date-card__seats">4+ SEATS LEFT</p><span class="date-card__book">BOOK NOW</span></article>
      <article class="date-card"><div class="date-card__price"><small>FROM</small>US $2395</div>
        <p class="date-card__dates">JULY 28TH, 2019<br>AUG 2ND, 2019</p><p class="date-card__seats">4+ SEATS LEFT</p><span class="date-card__book">BOOK NOW</span></article>
      <article class="date-card"><div class="date-card__price"><small>FROM</small>US $2395</div>
        <p class="date-card__dates">SEPTEMBER 1ST, 2019<br>SEPTEMBER 6TH, 2019</p><p class="date-card__seats">4+ SEATS LEFT</p><span class="date-card__book">BOOK NOW</span></article>
      <article class="date-card"><div class="date-card__price"><small>FROM</small>US $2395</div>
        <p class="date-card__dates">SEPT 8TH, 2019<br>SEPT 13TH, 2019</p><p class="date-card__seats">4+ SEATS LEFT</p><span class="date-card__book">BOOK NOW</span></article>
    </div>
  </div>
</section>

</body>
</html>
```